依頼詳細
今ある幸せをメッセージとして書き、ご報告と共にお祈り頂きます。それ以外にも献歌などのサブ的なイベントのご案内を盛り込みたいと思います。
記載項目
詳細は添付資料をご確認願います。また、添付画像をご利用下さい。
サイズ
A4
ページ数
片面
希望イメージ
シンプル 複雑
単色 カラフル
暗い 明るい
日常 高級
遊び心 厳粛
未来的 伝統的
女性的 男性的
希望する色
納品ファイル
• イラストレーター形式 (.ai)
補足説明
アウトラインの有るもの、無いもの双方でお願い致します。添付画像は加工OKです。
■ 選んだ理由

選定にあたりましては弊社内でメイン画像枠の取り方(グラデーション/エッジ)で大きく選考しました。その結果、グラデーションが良いとの意見が過半数を超え、その中で更に投票方式によりhasuventoさんのご提案を選ばせて頂きました。慰霊そしてお客様へのメッセージが重要でありながら、サブイベントでは楽しさを感じさせ、行ってみたくなる。弊社が考えるコンセプトそのものでした。
また、度重なる修正依頼にも応じて頂けました事、本当に助かりました。

■ 提案者全員のお礼・コメント

皆様より本当に多くのご提案を頂きました事、この場をお借りし、御礼申し上げます。今回初めてポルメットへの依頼であり、ご提案頂けるのか不安がありましたが、ご応募頂いた皆様が当社のコンセプトをご理解・ご提案頂きました事また、その表現力、感謝の言葉しかありません。今後もお力を頂く機会があろうかと思いますし、是非、依頼をしたいと思います。その時にまたご提案頂く事が出来れば幸いです。

```html
<!DOCTYPE html>
<html lang="ja">
<head>
<meta charset="utf-8">
<title>キャンドル慰霊祭</title>
<link href="https://fonts.googleapis.com/css2?family=Shippori+Mincho:wght@400;600;700&family=Noto+Sans+JP:wght@400;500;700&display=swap" rel="stylesheet">
<style>
  :root {
    --paper: #f4ecdc;
    --paper-light: #fbf6ec;
    --night: #2a1a10;
    --night-mid: #4a2e1a;
    --flame: #e9b766;
    --ink: #4b2f1e;
    --ink-soft: #6d5140;
    --accent: #8a5a33;
    --white: #ffffff;
  }
  * { margin: 0; padding: 0; box-sizing: border-box; }
  html, body { width: 850px; height: 1200px; overflow: hidden; }
  body { background: var(--paper); font-family: "Noto Sans JP", sans-serif; color: var(--ink); }

  .flyer {
    position: relative; width: 850px; height: 1200px; overflow: hidden;
    background:
      radial-gradient(ellipse 60% 35% at 75% 70%, rgba(255,250,235,.9), rgba(255,250,235,0) 70%),
      radial-gradient(ellipse 50% 30% at 20% 95%, rgba(255,248,230,.8), rgba(255,248,230,0) 70%),
      linear-gradient(180deg, var(--paper-light) 0%, var(--paper) 100%);
  }

  .hero-band {
    position: absolute; left: 0; top: 0; width: 850px; height: 300px;
    background: linear-gradient(180deg, var(--night) 0%, var(--night) 55%, rgba(42,26,16,0) 100%);
  }
  .hero-photo {
    position: absolute; left: -120px; top: -140px; width: 860px; height: 760px;
    border-radius: 50%;
    background:
      radial-gradient(ellipse 30% 22% at 62% 78%, rgba(240,245,235,.95), rgba(160,190,140,.6) 55%, rgba(70,50,30,0) 100%),
      radial-gradient(ellipse 35% 40% at 35% 45%, rgba(233,183,102,.45), rgba(233,183,102,0) 70%),
      radial-gradient(ellipse 50% 50% at 50% 50%, var(--night-mid) 0%, var(--night) 60%, rgba(42,26,16,0) 72%);
  }

  .event-title {
    position: absolute; right: 40px; top: 30px;
    font-family: "Shippori Mincho", serif; font-weight: 600;
    font-size: 58px; letter-spacing: 4px; color: var(--white);
  }
  .message {
    position: absolute; left: 405px; top: 115px;
    font-family: "Shippori Mincho", serif; font-size: 14px; line-height: 2;
    color: var(--white);
  }

  .schedule { position: absolute; right: 45px; top: 505px; text-align: right; font-family: "Shippori Mincho", serif; color: var(--ink); }
  .schedule .date { font-size: 64px; font-weight: 600; line-height: 1; }
  .schedule .date .year { font-size: 28px; margin-right: 6px; }
  .schedule .time { font-size: 34px; font-weight: 600; margin-top: 8px; }
  .schedule .free { font-family: "Noto Sans JP", sans-serif; font-size: 20px; font-weight: 700; margin-top: 4px; }
  .schedule .note { font-family: "Noto Sans JP", sans-serif; font-size: 9px; line-height: 1.6; color: var(--ink-soft); margin-top: 10px; }

  .sub-event {
    position: absolute; border-radius: 50%;
    background: radial-gradient(circle, rgba(255,255,255,.98) 60%, rgba(255,255,255,.85) 75%, rgba(255,255,255,0) 100%);
    text-align: center; color: var(--ink);
  }
  .sub-event h2 { font-family: "Shippori Mincho", serif; font-weight: 700; font-size: 30px; line-height: 1.25; color: var(--accent); }
  .sub-event .sub-time { font-size: 14px; font-weight: 500; margin-top: 4px; }
  .sub-event .detail { font-size: 9px; line-height: 1.6; color: var(--ink-soft); }
  .sub-event .thumb { border-radius: 50%; }

  .song { left: 20px; top: 620px; width: 300px; height: 300px; padding-top: 60px; }
  .song h2 { letter-spacing: 10px; }
  .song .row { display: flex; gap: 10px; justify-content: center; margin-top: 12px; align-items: center; }
  .song .thumb { width: 80px; height: 80px; background: radial-gradient(circle at 50% 40%, #e9d8c2, #a98a6d); border-radius: 10px; }
  .song .detail { text-align: left; width: 120px; }

  .flowers { left: 330px; top: 715px; width: 280px; height: 280px; padding-top: 50px; }
  .flowers h2 { font-size: 26px; }
  .flowers .thumb { width: 110px; height: 110px; margin: 12px auto 0; background: radial-gradient(circle at 45% 45%, #f1d3d6, #d98b8f 55%, #9db07f); }

  .wire-art { left: 565px; top: 850px; width: 280px; height: 280px; padding-top: 62px; }
  .wire-art h2 { font-size: 27px; }
  .wire-art .row { display: flex; gap: 8px; justify-content: center; margin-top: 10px; align-items: center; }
  .wire-art .detail { text-align: left; width: 100px; }
  .wire-art .thumb { width: 86px; height: 86px; background: radial-gradient(circle at 50% 45%, #ffffff, #d9d2c6 60%, #9c8a77); }

  .brand { position: absolute; left: 26px; top: 1085px; width: 150px; text-align: center; color: var(--accent); font-family: "Shippori Mincho", serif; }
  .brand .mark { width: 46px; height: 46px; border-radius: 50%; background: var(--accent); margin: 0 auto 8px; }
  .brand .name { font-size: 13px; font-weight: 600; letter-spacing: 1px; line-height: 1.4; }

  .apply { position: absolute; left: 185px; top: 1132px; width: 560px; }
  .apply .label { display: inline-block; background: var(--accent); color: var(--white); font-size: 11px; padding: 2px 12px; border-radius: 2px; }
  .apply .body { border-top: 1px solid var(--accent); margin-top: 4px; padding-top: 6px; font-size: 10px; line-height: 1.6; color: var(--ink); }
  .apply .office { display: flex; justify-content: space-between; font-size: 11px; font-weight: 500; }
</style>
</head>
<body>
<main class="flyer">
  <div class="hero-band"></div>
  <div class="hero-photo" role="img" aria-label="暗がりに並ぶキャンドルの灯りと、メッセージ帳を囲むあじさいの花の写真"></div>

  <h1 class="event-title">キャンドル慰霊祭</h1>
  <p class="message">
    先だったかたの願い<br>
    それは遺された方々が<br>
    日々の生活を幸せに送ることではないでしょうか<br>
    いつも見守ってくれている大切な人へ<br>
    あの頃のこと、今日のこと、これからのこと<br>
    家族みんなの笑顔とともにメッセージとし<br>
    お届けしてはいかがでしょうか
  </p>

  <section class="schedule">
    <div class="date"><span class="year">2016</span>7/16</div>
    <div class="time">14:00 ～18:00</div>
    <div class="free">入場無料</div>
    <p class="note">ご家族そろってのご参加をお待ちしております。<br>当日はお気軽に会場へお越しください。</p>
  </section>

  <section class="sub-event song">
    <h2>献歌</h2>
    <div class="sub-time">14:30～16:00</div>
    <div class="row">
      <div class="thumb" role="img" aria-label="歌い手の写真"></div>
      <p class="detail">春野 みなと<br>地元で活動する歌い手による<br>やさしい歌声をお届けします</p>
    </div>
  </section>

  <section class="sub-event flowers">
    <h2>お花の<br>プレゼント</h2>
    <div class="thumb" role="img" aria-label="小さな花束の写真"></div>
  </section>

  <section class="sub-event wire-art">
    <h2>モールアート</h2>
    <div class="sub-time">先着30名様 16:30～</div>
    <div class="row">
      <p class="detail">モールを使って<br>かわいい作品を<br>一緒に作りましょう</p>
      <div class="thumb" role="img" aria-label="モールで作った白い動物の作品の写真"></div>
    </div>
  </section>

  <div class="brand">
    <div class="mark"></div>
    <div class="name">CEREMONY HOTEL<br>KOHAKU</div>
  </div>

  <section class="apply">
    <span class="label">お申し込み方法</span>
    <div class="body">
      <p>お手数ですが、返信用紙にご記入の上、7月11日までに返信封筒にてご郵送をお願いします。</p>
      <div class="office"><span>2016キャンドル慰霊祭事務局</span><span>桜台町3丁目8-12　TEL 0120-000-000</span></div>
    </div>
  </section>
</main>
</body>
</html>
```